Business card for auto dealership

Looking for a clean modern design.
Would like attached logo incorporated

Industry/Entity Type

Car dealership

Contact Information for Business Card

Name, website, phone, cell, fax, email

```html
<!DOCTYPE html>
<html lang="en">
<head>
<meta charset="utf-8">
<title>Halverson Truck &amp; Auto Sales — Business Card</title>
<link rel="stylesheet" href="https://fonts.googleapis.com/css2?family=Lato:wght@400;700&display=swap">
<style>
  :root {
    --page-bg: #e9e9e9;
    --card-bg: #f7f7f7;
    --tone-light: #f4f4f4;
    --tone-mid: #e2e2e2;
    --ink: #111111;
    --ink-soft: #555555;
    --ink-body: #333333;
    --band: #0b0b0b;
  }
  * { box-sizing: border-box; margin: 0; padding: 0; }
  html, body { width: 1200px; height: 900px; overflow: hidden; }
  body {
    background: var(--page-bg);
    font-family: "Lato", Arial, sans-serif;
    color: var(--ink);
    display: flex;
    flex-direction: column;
    align-items: center;
    justify-content: center;
    gap: 40px;
  }
  .card {
    position: relative;
    width: 700px;
    height: 400px;
    background: var(--card-bg);
    overflow: hidden;
    box-shadow: 0 6px 18px rgba(0,0,0,0.18);
  }
  .card__backdrop {
    position: absolute;
    left: 0; right: 0; top: 0; bottom: 30px;
    background: linear-gradient(120deg, var(--tone-light) 0%, var(--tone-mid) 45%, var(--tone-light) 100%);
  }
  .card__band {
    position: absolute; left: 0; right: 0; bottom: 0;
    height: 30px; background: var(--band);
  }
  .brand {
    position: absolute;
    display: flex; flex-direction: column; align-items: flex-end;
    line-height: 1;
  }
  .brand__name {
    font-weight: 700;
    font-size: 64px;
    letter-spacing: -1px;
    color: var(--ink);
  }
  .brand__tagline {
    font-weight: 700;
    font-size: 14px;
    letter-spacing: 1.5px;
    color: var(--ink);
    margin-top: 4px;
  }
  .card--front .brand { left: 50%; top: 150px; transform: translateX(-50%); }
  .card--back .brand { left: 60px; top: 220px; }
  .brand--compact .brand__name { font-size: 52px; }
  .brand--compact .brand__tagline { font-size: 12px; }
  .divider {
    position: absolute; left: 380px; top: 100px;
    width: 1px; height: 200px; background: var(--ink);
  }
  .contact { position: absolute; left: 410px; top: 95px; }
  .contact__name { font-size: 19px; font-weight: 700; letter-spacing: 0.5px; }
  .contact__role { font-size: 15px; color: var(--ink-soft); margin-bottom: 16px; }
  .contact__list { list-style: none; }
  .contact__item {
    display: flex; align-items: center; gap: 10px;
    font-size: 15px; color: var(--ink-body); height: 24px;
    white-space: nowrap;
  }
  .contact__icon { width: 16px; height: 16px; flex: none; }
</style>
</head>
<body>

<section class="card card--front" aria-label="Card front">
  <div class="card__backdrop" role="img" aria-label="Soft grey abstract curved background shapes"></div>
  <div class="brand">
    <span class="brand__name">Halverson</span>
    <span class="brand__tagline">TRUCK &amp; AUTO SALES</span>
  </div>
  <div class="card__band"></div>
</section>

<section class="card card--back" aria-label="Card back">
  <div class="card__backdrop" role="img" aria-label="Soft grey abstract curved background shapes"></div>

  <div class="brand brand--compact">
    <span class="brand__name">Halverson</span>
    <span class="brand__tagline">TRUCK &amp; AUTO SALES</span>
  </div>

  <div class="divider"></div>

  <div class="contact">
    <p class="contact__name">DANIEL REYES</p>
    <p class="contact__role">Director</p>
    <ul class="contact__list">
      <li class="contact__item">
        <svg class="contact__icon" viewBox="0 0 16 16" aria-hidden="true"><rect x="4" y="1" width="8" height="14" rx="1.5" fill="none" stroke="#222" stroke-width="1.2"/><circle cx="8" cy="12.5" r="0.8" fill="#222"/></svg>
        555-201-4470
      </li>
      <li class="contact__item">
        <svg class="contact__icon" viewBox="0 0 16 16" aria-hidden="true"><path d="M2 6 C2 3 14 3 14 6 L12 7 L10 5.5 H6 L4 7 Z" fill="#222"/><rect x="3" y="8" width="10" height="6" rx="1" fill="#222"/></svg>
        555-201-4470
      </li>
      <li class="contact__item">
        <svg class="contact__icon" viewBox="0 0 16 16" aria-hidden="true"><rect x="4" y="1.5" width="8" height="5" fill="none" stroke="#222" stroke-width="1.2"/><rect x="1.5" y="7" width="13" height="6" rx="1" fill="none" stroke="#222" stroke-width="1.2"/><line x1="4" y1="10" x2="12" y2="10" stroke="#222" stroke-width="1.2"/></svg>
        555-201-4488
      </li>
      <li class="contact__item">
        <svg class="contact__icon" viewBox="0 0 16 16" aria-hidden="true"><rect x="1.5" y="3.5" width="13" height="9" rx="1" fill="#222"/><path d="M2 4.5 L8 9 L14 4.5" fill="none" stroke="#fff" stroke-width="1.2"/></svg>
        info@halversonauto.com
      </li>
      <li class="contact__item">
        <svg class="contact__icon" viewBox="0 0 16 16" aria-hidden="true"><circle cx="8" cy="8" r="6.5" fill="none" stroke="#222" stroke-width="1.2"/><ellipse cx="8" cy="8" rx="3" ry="6.5" fill="none" stroke="#222" stroke-width="1"/><line x1="1.5" y1="8" x2="14.5" y2="8" stroke="#222" stroke-width="1"/></svg>
        www.halversonauto.com
      </li>
    </ul>
  </div>

  <div class="card__band"></div>
</section>

</body>
</html>
```